DebtHarbor.com website design

We are a collection agency that collects debt from past residents of apartments on behalf of Property Management Companies. We are want to design a 3 page website with - Home - How it Works - Schedule Demo. We'd like a sketch of a skyline showing high rise apartment buildings, houses, shops, etc. We would like for there to be some animation, possibly clouds and the sun slowly moving. Maybe kids playing ball or catch or something like that. Bird flying and landing. An electric car charging (to indicate we are modern). We are looking for a friendly community vibe. The site will also need a button "Property Managers Login". When some comes to the site we would like a pop up that says "Property Managers Click Here/Past Residents Click Here" with a different icon for each that relates to the description. I've included a link to a test site we had designed so feel free to use some of the copy from it. We just aren't happy with the design. On the Home page our tag line should be "Get more payments, faster, from past residents!" and "Digital First, NOT Digital Only". All without transaction fees, we don't get paid unless we get you paid first!
Additional selling points:

24 hour virtual agent and virtual telephone agent so we don't miss any opportunities to GET YOUR MONEY!

Old school collection strategies meet cutting edge technology to create effective work flow algorithms to put the best debt collectors on your accounts with data driven intelligence to determine the best way to get paid.

No Subscription Fees
No Payment Processing Fees
No Software Fees
No Mail, Email or TXT Fees

Inquire about our FIRST PARTY accounts receivable outsourcing. You may qualify for free post move out A/R processing and AI payment negotiator for the low hanging fruit. Don't pay full collection commission when there wasn't a full collection attempt!

For the How it Works page - See the page from our previous design. I will include the link below. Please come up with your own version of this but you can use the copy from this page.

The schedule demo page will be a form that will feed to our CRM that will include:
Name
Email
Company
Title
Phone Number
Number of Units
Tell us how we can help you: (a box for them provide details)

Also include our phone number at the bottom with something like

Here is a link to our previous design test site:
https://brisklane-preview.net/debtharbor-new/
I've attached an image of the back end so you can get an idea of the colors we need, I've also included our logo. For the most part we would like most of the site to match the blue colors from our logo, but we do need to incorporate some of the yellow in the images I've attached. Possibly make the buttons on the site the yellow color? Make the sun Match the yellow? I'll leave it up to you.

```html
<!DOCTYPE html>
<html lang="en">
<head>
<meta charset="utf-8">
<title>DebtHarbor – Debt Recovery Management</title>
<link href="https://fonts.googleapis.com/css2?family=Barlow+Semi+Condensed:wght@500;600;700&family=Poppins:wght@400;500&display=swap" rel="stylesheet">
<style>
:root{
  --navy:#0b3a66;
  --navy-deep:#082f55;
  --teal:#1cb2cc;
  --orange:#ffa41b;
  --peach:#fde9d6;
  --text:#555b66;
  --white:#ffffff;
}
*{margin:0;padding:0;box-sizing:border-box}
html,body{width:1200px;height:3027px;overflow:hidden}
body{position:relative;background:var(--white);font-family:"Poppins",sans-serif;color:var(--text)}
.head{font-family:"Barlow Semi Condensed",sans-serif}
.abs{position:absolute}

/* hero */
.hero{left:0;top:0;width:1200px;height:837px;background:linear-gradient(180deg,var(--peach) 0%,#fff3e8 40%,#fbeee3 100%)}
.hero-scene{left:0;top:360px;width:1200px;height:477px;background:linear-gradient(180deg,#fbeee3 0%,#f7d9c4 35%,#9fd2c8 62%,#95cfc6 100%)}
.brand{left:149px;top:40px;display:flex;align-items:center;gap:10px}
.brand-dot{width:34px;height:34px;border-radius:50%;background:var(--teal)}
.brand-name{font-family:"Barlow Semi Condensed",sans-serif;font-weight:600;font-size:32px;color:var(--navy);line-height:1}
.nav{top:44px;font-family:"Barlow Semi Condensed",sans-serif;font-weight:600;font-size:16px;color:var(--navy)}
.login-btn{left:828px;top:30px;width:220px;height:43px;border-radius:22px;background:var(--orange);color:#fff;font-family:"Barlow Semi Condensed",sans-serif;font-weight:600;font-size:16px;display:flex;align-items:center;justify-content:center}
.hero-title{left:0;top:180px;width:1200px;text-align:center;font-weight:600;font-size:44px;line-height:52px;color:var(--navy)}
.hero-sub{left:0;top:292px;width:1200px;text-align:center;font-weight:600;font-size:33px;color:var(--teal)}
.hero-note{left:0;top:341px;width:1200px;text-align:center;font-weight:600;font-size:14px;color:#222}

/* welcome */
.welcome-title{left:0;top:916px;width:1200px;text-align:center;font-weight:600;font-size:46px;color:var(--navy)}
.welcome-text{left:330px;top:985px;width:540px;text-align:center;font-size:14.5px;line-height:21px;color:#555}
.choice{width:270px;height:270px;border-radius:50%;top:1072px;display:flex;flex-direction:column;align-items:center;justify-content:center;color:#fff}
.choice-manager{left:340px;background:radial-gradient(circle at 60% 40%,#1d5a8c,var(--navy-deep))}
.choice-resident{left:590px;background:radial-gradient(circle at 40% 40%,#3dc1da,#1aa6c3);border:6px solid #fff;width:282px;height:282px;top:1066px}
.choice h3{font-family:"Barlow Semi Condensed",sans-serif;font-weight:600;font-size:24px;line-height:22px;text-align:center;margin-top:12px}
.choice a{font-family:"Barlow Semi Condensed",sans-serif;font-weight:600;font-size:15px;text-decoration:underline;margin-top:16px}
.choice-manager a{color:var(--teal)}
.choice-resident a{color:var(--navy)}

/* grey band */
.band{left:0;top:1378px;width:1200px;height:1090px;background:linear-gradient(180deg,#f1f1f2 0%,#f4f4f5 60%,#fdfdfd 100%)}
.agent-title{left:149px;top:1618px;width:495px;font-weight:600;font-size:42px;line-height:48px;color:var(--navy)}
.agent-title span{color:var(--orange)}
.agent-text{left:149px;top:1835px;width:500px;font-size:15.5px;line-height:24.5px;color:#6b6f78}
.agent-art{left:699px;top:1607px;width:355px;height:341px;border-radius:50%;background:radial-gradient(circle,#f6dcc0 0%,#dcebf3 55%,#f3f3f4 75%)}
.feature{top:2023px;width:176px;height:168px;background:#fff;border:1.5px solid var(--teal);border-radius:10px;box-shadow:0 4px 10px rgba(0,0,0,.08);display:flex;flex-direction:column;align-items:center;padding-top:26px}
.feature p{font-family:"Barlow Semi Condensed",sans-serif;font-weight:600;font-size:17px;line-height:18px;text-align:center;color:var(--navy);margin-top:14px}
.inquire{left:190px;top:2277px;width:820px;text-align:center;font-family:"Barlow Semi Condensed",sans-serif;font-weight:500;font-size:23px;line-height:33px;color:#555}
.inquire a{color:var(--teal);font-weight:600;text-decoration:underline}

/* footer */
.footer-bg{left:0;top:2462px;width:1200px;height:565px}
.footer-brand{left:0;top:2604px;width:1200px;display:flex;justify-content:center;align-items:center;gap:14px}
.footer-brand .brand-dot{width:56px;height:56px}
.footer-brand .brand-name{font-size:52px;color:#fff}
.col-title{top:2712px;font-family:"Barlow Semi Condensed",sans-serif;font-weight:600;font-size:33px;color:var(--teal)}
.divider{top:2720px;width:1px;height:224px;background:rgba(255,255,255,.18)}
.f-link{font-size:13px;color:#fff}
.contact-row{left:149px;display:flex;align-items:center;gap:12px;font-size:12.5px;line-height:17px;color:#fff}
.c-icon{width:32px;height:32px;border-radius:50%;border:1.5px solid var(--teal);display:flex;align-items:center;justify-content:center;flex:none}
.social{left:928px;display:flex;align-items:center;gap:12px;font-size:13px;color:#fff}
.s-dot{width:14px;height:14px;border-radius:50%;background:#fff}
.copy{left:0;top:2974px;width:1200px;text-align:center;font-size:11px;color:#fff}
</style>
</head>
<body>

<section class="abs hero"></section>
<div class="abs hero-scene" role="img" aria-label="Illustrated neighbourhood skyline with houses, apartment blocks, a bakery, children playing ball, birds, the sun and an electric car charging"></div>

<header>
  <div class="abs brand"><span class="brand-dot"></span><span class="brand-name">DebtHarbor</span></div>
  <a class="abs nav" style="left:449px">Home</a>
  <a class="abs nav" style="left:537px">How it Works</a>
  <a class="abs nav" style="left:674px">Schedule Demo</a>
  <a class="abs login-btn">Property Managers Login</a>
</header>

<h1 class="abs head hero-title">Get more payments,<br>faster, from past residents!</h1>
<p class="abs head hero-sub">Digital First, NOT Digital Only</p>
<p class="abs head hero-note">All without transaction fees, we don't get paid unless we get you paid first!</p>

<h2 class="abs head welcome-title">Welcome to DebtHarbor</h2>
<p class="abs welcome-text">We ensure that you maintain your valued image by using an ethical and respectful, while the aggressive, approach to your debt recovery services.</p>

<div class="abs choice choice-manager" role="img" aria-label="Property managers option over a photo of a team in an office">
  <svg width="72" height="72" viewBox="0 0 72 72" fill="none" stroke="#fff" stroke-width="2.5"><circle cx="26" cy="20" r="10"/><path d="M8 60c0-12 8-20 18-20s18 8 18 20"/><path d="M40 38l14-10 14 10v24H40z"/><rect x="50" y="48" width="8" height="14"/></svg>
  <h3>Property<br>Managers</h3><a>Click Here</a>
</div>
<div class="abs choice choice-resident" role="img" aria-label="Past residents option over a photo of a family">
  <svg width="72" height="72" viewBox="0 0 72 72" fill="none" stroke="#fff" stroke-width="2.5"><path d="M8 34L36 10l28 24"/><path d="M16 28v34h40V28"/><circle cx="28" cy="38" r="5"/><circle cx="44" cy="38" r="5"/><path d="M20 58c0-8 4-12 8-12s8 4 8 12M36 58c0-8 4-12 8-12s8 4 8 12"/></svg>
  <h3>Past<br>Residents</h3><a>Click Here</a>
</div>

<div class="abs band"></div>
<svg class="abs" style="left:0;top:1378px" width="1200" height="90" viewBox="0 0 1200 90"><polygon points="0,0 1200,0 1200,12 584,87 0,0" fill="#fff"/></svg>

<h2 class="abs head agent-title">24 hour virtual agent and virtual telephone agent so we don't miss any opportunities to <span>GET YOUR MONEY!</span></h2>
<p class="abs agent-text">Old school collection strategies meet cutting edge technology to create effective work flow algorithms to put the best debt collectors on your accounts with data driven intelligence to determine the best way to get paid.</p>
<div class="abs agent-art" role="img" aria-label="Illustration of a virtual support agent with headset at a computer talking with a resident on the phone"></div>

<div class="abs feature" style="left:184px">
  <svg width="56" height="56" viewBox="0 0 56 56" fill="none" stroke="var(--navy)" stroke-width="2"><rect x="6" y="6" width="44" height="26" rx="2"/><path d="M22 52V26a4 4 0 018 0v10l8 2v14"/></svg>
  <p>No Subscription<br>Fees</p>
</div>
<div class="abs feature" style="left:396px">
  <svg width="56" height="56" viewBox="0 0 56 56" fill="none" stroke="var(--navy)" stroke-width="2"><circle cx="28" cy="28" r="24"/><rect x="14" y="20" width="28" height="16" rx="2"/><path d="M11 11l34 34" stroke="var(--teal)"/></svg>
  <p>No Payment<br>Processing Fees</p>
</div>
<div class="abs feature" style="left:602px">
  <svg width="56" height="56" viewBox="0 0 56 56" fill="none" stroke="var(--navy)" stroke-width="2"><rect x="4" y="8" width="48" height="34" rx="2"/><path d="M20 50h16M28 42v8M22 20l-6 5 6 5M34 20l6 5-6 5M30 18l-4 14"/></svg>
  <p>No Software<br>Fees</p>
</div>
<div class="abs feature" style="left:808px">
  <svg width="56" height="56" viewBox="0 0 56 56" fill="none" stroke="var(--navy)" stroke-width="2"><path d="M4 22l24-16 24 16v28H4z"/><path d="M4 22l24 18 24-18"/><circle cx="28" cy="20" r="6" stroke="var(--teal)"/></svg>
  <p>No Mail, Email<br>or TXT Fees</p>
</div>

<p class="abs inquire">Inquire about our <a>FIRST PARTY</a> accounts receivable outsourcing. You may qualify for free post move out A/R processing and AI payment negotiator for the low hanging fruit. Don't pay full collection commission when there wasn't a full collection attempt!</p>

<footer>
  <svg class="abs footer-bg" width="1200" height="565" viewBox="0 0 1200 565"><polygon points="0,0 584,86 1200,0 1200,565 0,565" fill="var(--navy-deep)"/></svg>
  <div class="abs footer-brand"><span class="brand-dot"></span><span class="brand-name">DebtHarbor</span></div>

  <h4 class="abs col-title" style="left:153px">Contact Us</h4>
  <h4 class="abs col-title" style="left:467px">Links</h4>
  <h4 class="abs col-title" style="left:717px">Menu</h4>
  <h4 class="abs col-title" style="left:923px">Connect</h4>
  <span class="abs divider" style="left:411px"></span>
  <span class="abs divider" style="left:654px"></span>
  <span class="abs divider" style="left:855px"></span>

  <div class="abs contact-row" style="top:2780px"><span class="c-icon"><svg width="14" height="14" viewBox="0 0 24 24" fill="var(--teal)"><path d="M6.6 10.8a15 15 0 006.6 6.6l2.2-2.2a1 1 0 011-.25 11.4 11.4 0 003.6.6 1 1 0 011 1V20a1 1 0 01-1 1A17 17 0 013 4a1 1 0 011-1h3.5a1 1 0 011 1 11.4 11.4 0 00.6 3.6 1 1 0 01-.25 1z"/></svg></span><span>Phone:<br>555 0142 7730</span></div>
  <div class="abs contact-row" style="top:2836px"><span class="c-icon"><svg width="14" height="14" viewBox="0 0 24 24" fill="none" stroke="var(--teal)" stroke-width="2.5"><rect x="3" y="5" width="18" height="14" rx="2"/><path d="M3 7l9 6 9-6"/></svg></span><span>Email:<br>hello@debtharbor.com</span></div>
  <div class="abs contact-row" style="top:2894px"><span class="c-icon"><svg width="14" height="14" viewBox="0 0 24 24" fill="none" stroke="var(--teal)" stroke-width="2.5"><path d="M12 22s7-7 7-12a7 7 0 00-14 0c0 5 7 12 7 12z"/><circle cx="12" cy="10" r="2.5"/></svg></span><span>123 ipsum dolor sit amet, con<br>ectetur adipiscing elit</span></div>

  <a class="abs f-link" style="left:469px;top:2780px">Property Managers</a>
  <a class="abs f-link" style="left:469px;top:2815px">Past Residents</a>
  <a class="abs f-link" style="left:469px;top:2850px">Property Managers Login</a>
  <a class="abs f-link" style="left:469px;top:2885px">GET YOUR MONEY!</a>

  <a class="abs f-link" style="left:719px;top:2780px">Home</a>
  <a class="abs f-link" style="left:719px;top:2815px">How it Works</a>
  <a class="abs f-link" style="left:719px;top:2850px">Schedule Demo</a>

  <a class="abs social" style="top:2781px"><span class="s-dot"></span>Workline</a>
  <a class="abs social" style="top:2816px"><span class="s-dot"></span>Circlebook</a>
  <a class="abs social" style="top:2851px"><span class="s-dot"></span>Snapgrid</a>

  <p class="abs copy">©2022 DebtHarbor. All rights reserved. Privacy Policy Terms of Service</p>
</footer>

</body>
</html>
```